Business Card Design Project

"Crestline Record Services" is database management company working in the direct marketing & digital printing industries. Currently going through a name & rebranding process we require a new company business card.

Industry/Entity Type

Marketing

```html
<!DOCTYPE html>
<html lang="en">
<head>
<meta charset="utf-8">
<title>Crestline Record Services – Business Card</title>
<link rel="stylesheet" href="https://fonts.googleapis.com/css2?family=Ubuntu:wght@400;500&display=swap">
<style>
  :root {
    --backdrop: #2f3032;
    --card-white: #ffffff;
    --blue-deep: #1b86c8;
    --blue-light: #33ace0;
    --ink-grey: #565d66;
    --swoosh-grey: #5a5f68;
    --text-white: #ffffff;
  }
  * { box-sizing: border-box; margin: 0; padding: 0; }
  html, body {
    width: 1200px; height: 900px; overflow: hidden;
    background: var(--backdrop);
    font-family: "Ubuntu", sans-serif;
  }
  .stage { position: relative; width: 1200px; height: 900px; }
  .card {
    position: absolute; top: 308px; width: 513px; height: 284px;
    border-radius: 16px; overflow: hidden; background: var(--card-white);
    box-shadow: 0 4px 10px rgba(0,0,0,0.45);
  }
  .card--front { left: 72px; }
  .card--back { left: 615px; }
  .card-bg { position: absolute; inset: 0; width: 100%; height: 100%; }

  .wordmark {
    position: absolute; left: 0; right: 0;
    display: flex; align-items: center; justify-content: center; gap: 12px;
    font-weight: 500; font-size: 29px; letter-spacing: 0.2px; white-space: nowrap;
  }
  .wordmark-dot { width: 16px; height: 16px; border-radius: 50%; flex: none; }
  .card--front .wordmark { top: 112px; color: var(--text-white); }
  .card--front .wordmark-dot { background: var(--text-white); }
  .card--back .wordmark { top: 58px; color: var(--ink-grey); }
  .card--back .wordmark-dot { background: var(--blue-deep); }

  .front-contacts {
    position: absolute; left: 0; right: 0; top: 250px;
    display: flex; justify-content: center; gap: 8px;
    font-size: 13.5px; color: var(--ink-grey);
  }
  .contact-item { display: flex; align-items: center; gap: 4px; white-space: nowrap; }
  .icon { width: 11px; height: 11px; flex: none; }
  .front-contacts .icon { fill: var(--ink-grey); }

  .person { position: absolute; left: 33px; top: 176px; color: var(--text-white); }
  .person-name { font-size: 21px; font-weight: 400; line-height: 1.1; }
  .person-title { font-size: 15px; line-height: 1.3; margin-left: 2px; }

  .back-contacts {
    position: absolute; color: var(--text-white); font-size: 14px; line-height: 19.5px;
  }
  .back-contacts .icon { fill: var(--text-white); }
  .back-contacts--online { left: 34px; top: 227px; }
  .back-contacts--office { left: 305px; top: 188px; }
  .indent { padding-left: 15px; }
</style>
</head>
<body>
<main class="stage">

  <section class="card card--front" aria-label="Card front">
    <svg class="card-bg" viewBox="0 0 513 284" preserveAspectRatio="none" aria-hidden="true">
      <defs>
        <radialGradient id="frontBlue" cx="0.55" cy="0.2" r="0.8">
          <stop offset="0" stop-color="#3bb3e4"/>
          <stop offset="1" stop-color="#1b86c8"/>
        </radialGradient>
      </defs>
      <path d="M0 0 H513 V220 Q300 196 0 186 Z" fill="url(#frontBlue)"/>
      <path d="M140 222 Q340 232 513 214 L513 224 Q340 242 140 222 Z" fill="#5a5f68"/>
    </svg>
    <div class="wordmark"><span class="wordmark-dot"></span>Crestline Record Services</div>
    <div class="front-contacts">
      <span class="contact-item">
        <svg class="icon" viewBox="0 0 12 12"><path d="M0 2h12v8H0z M0 2l6 4 6-4" fill="currentColor"/><path d="M0.5 2.5l5.5 3.6 5.5-3.6" fill="none" stroke="#fff" stroke-width="1"/></svg>
        info@crestlinerecords.com
      </span>
      <span class="contact-item">
        <svg class="icon" viewBox="0 0 12 12"><circle cx="6" cy="6" r="5.5"/><path d="M0.5 6h11M6 0.5v11M2 3h8M2 9h8" stroke="#fff" stroke-width="0.8" fill="none"/><ellipse cx="6" cy="6" rx="2.5" ry="5.5" fill="none" stroke="#fff" stroke-width="0.8"/></svg>
        www.crestlinerecords.com
      </span>
    </div>
  </section>

  <section class="card card--back" aria-label="Card back">
    <svg class="card-bg" viewBox="0 0 513 284" preserveAspectRatio="none" aria-hidden="true">
      <defs>
        <radialGradient id="backBlue" cx="0.45" cy="0.3" r="0.9">
          <stop offset="0" stop-color="#36aee2"/>
          <stop offset="1" stop-color="#1a80c2"/>
        </radialGradient>
      </defs>
      <path d="M0 126 Q220 146 450 150 Q220 160 0 142 Z" fill="#5a5f68"/>
      <path d="M0 146 Q250 172 513 160 V284 H0 Z" fill="url(#backBlue)"/>
    </svg>
    <div class="wordmark"><span class="wordmark-dot"></span>Crestline Record Services</div>

    <div class="person">
      <div class="person-name">Daniel Whitcombe</div>
      <div class="person-title">managing director</div>
    </div>

    <div class="back-contacts back-contacts--online">
      <div class="contact-item">
        <svg class="icon" viewBox="0 0 12 12"><path d="M0 2h12v8H0z"/><path d="M0.5 2.5l5.5 3.6 5.5-3.6" fill="none" stroke="#2494d2" stroke-width="1"/></svg>
        info@crestlinerecords.com
      </div>
      <div class="contact-item">
        <svg class="icon" viewBox="0 0 12 12"><circle cx="6" cy="6" r="5.5"/><path d="M0.5 6h11M6 0.5v11M2 3h8M2 9h8" stroke="#2494d2" stroke-width="0.8" fill="none"/><ellipse cx="6" cy="6" rx="2.5" ry="5.5" fill="none" stroke="#2494d2" stroke-width="0.8"/></svg>
        www.crestlinerecords.com
      </div>
    </div>

    <div class="back-contacts back-contacts--office">
      <div class="contact-item">
        <svg class="icon" viewBox="0 0 12 12"><path d="M6 0a4 4 0 0 1 4 4c0 3-4 8-4 8S2 7 2 4a4 4 0 0 1 4-4z"/><circle cx="6" cy="4" r="1.5" fill="#2494d2"/></svg>
        48 Harbor Lane
      </div>
      <div class="indent">Millbrook, New York 12545</div>
      <div class="contact-item">
        <svg class="icon" viewBox="0 0 12 12"><rect x="3" y="0" width="6" height="12" rx="1"/><rect x="4" y="1.5" width="4" height="7.5" fill="#2494d2"/></svg>
        555 214 67 90
      </div>
      <div class="contact-item">
        <svg class="icon" viewBox="0 0 12 12"><rect x="3" y="0" width="6" height="3"/><rect x="0" y="4" width="12" height="5" rx="1"/><rect x="3" y="7" width="6" height="5"/></svg>
        555 380 12 44
      </div>
    </div>
  </section>

</main>
</body>
</html>
```